Looking to design a new sign for our church.

Looking for a new sign
4 x 8 feet dimension
We are renaming the church "Medlow Ridge Community Church"
looking for legible graphics
Would like some type of backdrop being a family tree (oak) / open to other ideas as you are led
I have included a pic of the old sign for your review
would like to incorporate our ministry logo on the lower right hand corner of the sign / see file attached

```html
<!DOCTYPE html>
<html lang="en">
<head>
<meta charset="UTF-8">
<title>Medlow Ridge Community Church – Sign</title>
<link href="https://fonts.googleapis.com/css2?family=Barlow+Condensed:wght@800&family=Plus+Jakarta+Sans:wght@700;800&display=swap" rel="stylesheet">
<style>
  :root {
    --navy: #22289e;
    --cyan: #0db8f8;
    --cyan-shadow: #1ab8f5;
    --white: #ffffff;
    --sky-deep: #3f9fe6;
    --sky-mid: #9fcdf3;
    --sky-light: #f6faff;
  }
  * { margin: 0; padding: 0; box-sizing: border-box; }
  html, body { width: 1200px; height: 600px; overflow: hidden; }
  body { background: var(--white); }
  .sign {
    position: relative;
    width: 1200px;
    height: 600px;
    overflow: hidden;
    background: var(--sky-light);
  }
  .sky-backdrop {
    position: absolute;
    inset: 0;
    background:
      radial-gradient(ellipse 420px 260px at 1120px 60px, rgba(63,159,230,0.95), rgba(63,159,230,0) 75%),
      radial-gradient(ellipse 360px 300px at 0px 600px, rgba(159,205,243,0.95), rgba(159,205,243,0) 75%),
      radial-gradient(ellipse 300px 200px at 820px 60px, rgba(190,220,248,0.7), rgba(190,220,248,0) 80%),
      linear-gradient(120deg, var(--sky-mid) 0%, var(--sky-light) 28%, var(--white) 55%, var(--sky-light) 72%, var(--sky-mid) 100%);
  }
  .church-name {
    position: absolute;
    left: 54px;
    top: 24px;
    font-family: "Barlow Condensed", sans-serif;
    font-weight: 800;
    font-size: 152px;
    line-height: 120px;
    letter-spacing: 0.5px;
    color: var(--navy);
    text-shadow: 3px 3px 0 var(--cyan-shadow);
  }
  .services-band {
    position: absolute;
    left: 0;
    top: 321px;
    width: 630px;
    height: 66px;
  }
  .services-heading {
    position: absolute;
    left: 60px;
    top: 325px;
    height: 58px;
    line-height: 58px;
    font-family: "Plus Jakarta Sans", sans-serif;
    font-weight: 700;
    font-size: 42px;
    letter-spacing: -0.5px;
    color: var(--white);
  }
  .schedule {
    position: absolute;
    left: 58px;
    top: 398px;
    list-style: none;
    font-family: "Plus Jakarta Sans", sans-serif;
    font-weight: 700;
    font-size: 45px;
    line-height: 55px;
    color: var(--navy);
  }
  .schedule li { white-space: pre; }
  .ministry-mark {
    position: absolute;
    left: 1000px;
    top: 300px;
    width: 150px;
    display: flex;
    flex-direction: column;
    align-items: center;
    gap: 12px;
  }
  .ministry-dot {
    width: 70px;
    height: 70px;
    border-radius: 50%;
    background: var(--navy);
  }
  .ministry-name {
    font-family: "Plus Jakarta Sans", sans-serif;
    font-weight: 700;
    font-size: 20px;
    line-height: 24px;
    text-align: center;
    color: var(--navy);
  }
</style>
</head>
<body>
  <div class="sign">
    <div class="sky-backdrop" role="img" aria-label="Bright blue sky with soft white clouds and sun glow"></div>

    <h1 class="church-name">Medlow Ridge<br>Community Church</h1>

    <svg class="services-band" viewBox="0 0 630 66" aria-hidden="true">
      <polygon points="0,0 545,0 585,66 0,66" fill="var(--cyan)"/>
      <polygon points="554,0 582,0 622,66 596,66" fill="var(--navy)"/>
    </svg>
    <h2 class="services-heading">CHURCH SERVICES</h2>

    <ul class="schedule">
      <li>Sunday School    -  9:30am</li>
      <li>Worship Service  -  10:30am</li>
      <li>Wednesday Service - 6:00pm</li>
    </ul>

    <div class="ministry-mark">
      <div class="ministry-dot"></div>
      <p class="ministry-name">Harvest Light Ministries</p>
    </div>
  </div>
</body>
</html>
```